Seafood restaurant menu

I am looking for a new menu design for my cajun seafood restaurant. I want something modern and simple. Our menu is very small so just one page front and back. Preferred, menu size is (4.25"x11"), I have attach some images, but we will have more to give.
Updates

Need to give designer more time

Target Market(s)

young to middle aged customers

Industry/Entity Type

Restaurant Food industry

Colors
EB3D1F
EC4F4E
F09395
F8D3D4
FCEDEE

Requirements
Must have
• creativity and interesting
Nice to have
• I would like to see a clean and simple menu, but with good color placement and photos of the dishes

```html
<!DOCTYPE html>
<html lang="en">
<head>
<meta charset="utf-8">
<title>Gumbo's Crab Shack — Menu</title>
<link rel="stylesheet" href="https://fonts.googleapis.com/css2?family=Didact+Gothic&family=Kaushan+Script&display=swap">
<style>
  :root {
    --blush: #F5D2D3;
    --charcoal: #2A2A2A;
    --red: #E3262A;
    --heading-pink: #F8D3D4;
    --text-light: #F4F4F4;
    --circle-red: #EC4F4E;
  }
  * { margin: 0; padding: 0; box-sizing: border-box; }
  html, body { width: 1200px; height: 3107px; overflow: hidden; }
  body {
    position: relative;
    background: var(--blush);
    font-family: "Didact Gothic", Arial, sans-serif;
    color: var(--text-light);
  }
  .backdrop { position: absolute; left: 0; top: 0; }
  .brand-mark {
    position: absolute; left: 0; width: 1200px; top: 846px;
    text-align: center; font-size: 72px; line-height: 86px;
    font-variant: small-caps; color: #FFFFFF; letter-spacing: 1px;
  }
  .section-title {
    position: absolute; left: 243px;
    font-family: "Kaushan Script", cursive;
    color: var(--heading-pink); font-size: 84px; line-height: 110px;
  }
  .row {
    position: absolute; left: 141px; width: 888px; height: 44px;
    font-size: 37px; line-height: 44px; font-variant: small-caps;
  }
  .row .code { position: absolute; left: 0; top: 0; }
  .row .name { position: absolute; left: 112px; top: 0; }
  .row .price { position: absolute; right: 0; top: 0; }
  .note {
    position: absolute; font-size: 24px; line-height: 30px;
    font-variant: small-caps; text-transform: lowercase;
  }
  .divider { position: absolute; left: 141px; height: 32px; }
  .footer-mark {
    position: absolute; left: 0; width: 1200px; top: 3010px;
    text-align: center; font-size: 26px; line-height: 34px;
    font-variant: small-caps; color: var(--red);
  }
</style>
</head>
<body>
  <svg class="backdrop" width="1200" height="3107" viewBox="0 0 1200 3107">
    <polygon points="0,507 600,211 1200,507 1200,2964 0,2964" fill="var(--charcoal)"/>
    <circle cx="600" cy="560" r="190" fill="var(--circle-red)"/>
  </svg>

  <div class="brand-mark">Gumbo's Crab Shack</div>

  <h2 class="section-title" style="top:1056px">Appetizers</h2>
  <div class="row" style="top:1182px"><span class="code">A1</span><span class="name">8pc. Wings</span><span class="price">14</span></div>
  <p class="note" style="left:253px;top:1233px">(honey lemon pepper / buffalo / gumbos bomb)</p>
  <div class="row" style="top:1278px"><span class="code">A2</span><span class="name">Garlic Noodles</span><span class="price">7</span></div>

  <svg class="divider" style="top:1359px" width="230" height="32" viewBox="0 0 230 32">
    <rect x="0" y="0" width="14" height="14" fill="var(--red)"/><rect x="18" y="0" width="14" height="14" fill="var(--red)"/>
    <rect x="0" y="18" width="14" height="14" fill="var(--red)"/><rect x="18" y="18" width="14" height="14" fill="var(--red)"/>
    <rect x="57" y="14" width="165" height="4" fill="var(--red)"/>
  </svg>

  <h2 class="section-title" style="top:1420px">Fried Seafood Baskets</h2>
  <p class="note" style="left:247px;top:1547px">(served with a side: sweet potato fries or hush puppies +1)</p>
  <div class="row" style="top:1604px"><span class="code">F1</span><span class="name">Fried Oysters</span><span class="price">12</span></div>
  <div class="row" style="top:1662px"><span class="code">F2</span><span class="name">Fried Shrimp</span><span class="price">13</span></div>
  <div class="row" style="top:1720px"><span class="code">F3</span><span class="name">Fried Catfish</span><span class="price">12</span></div>
  <div class="row" style="top:1778px"><span class="code">F4</span><span class="name">Fried Calamari</span><span class="price">12</span></div>
  <div class="row" style="top:1836px"><span class="code">F5</span><span class="name">Soft Shell Crab*</span><span class="price">15</span></div>

  <svg class="divider" style="top:1909px" width="530" height="32" viewBox="0 0 530 32">
    <rect x="0" y="0" width="14" height="14" fill="var(--red)"/><rect x="18" y="0" width="14" height="14" fill="var(--red)"/>
    <rect x="0" y="18" width="14" height="14" fill="var(--red)"/><rect x="18" y="18" width="14" height="14" fill="var(--red)"/>
    <rect x="57" y="14" width="465" height="4" fill="var(--red)"/>
  </svg>

  <h2 class="section-title" style="top:1970px;left:265px">Sides</h2>
  <div class="row" style="top:2104px"><span class="code">S1</span><span class="name">Cajun Fries</span><span class="price">5</span></div>
  <div class="row" style="top:2162px"><span class="code">S2</span><span class="name">Sweet Potato Fries</span><span class="price">6</span></div>
  <div class="row" style="top:2220px"><span class="code">S3</span><span class="name">Hush Puppies</span><span class="price">6</span></div>
  <div class="row" style="top:2278px"><span class="code">S4</span><span class="name">Coleslaw</span><span class="price">4</span></div>
  <div class="row" style="top:2336px"><span class="code">S5</span><span class="name">Steamed Rice</span><span class="price">3</span></div>

  <svg class="divider" style="top:2415px" width="720" height="32" viewBox="0 0 720 32">
    <rect x="0" y="0" width="14" height="14" fill="var(--red)"/><rect x="18" y="0" width="14" height="14" fill="var(--red)"/>
    <rect x="0" y="18" width="14" height="14" fill="var(--red)"/><rect x="18" y="18" width="14" height="14" fill="var(--red)"/>
    <rect x="57" y="14" width="650" height="4" fill="var(--red)"/>
  </svg>

  <h2 class="section-title" style="top:2472px">Extras</h2>
  <div class="row" style="top:2607px"><span class="code">E1</span><span class="name">Potatoes (3pc)</span><span class="price">3</span></div>
  <div class="row" style="top:2665px"><span class="code">E2</span><span class="name">Corn on the cob (2pc)</span><span class="price">3</span></div>
  <div class="row" style="top:2723px"><span class="code">E3</span><span class="name">Boiled Eggs (2pc)</span><span class="price">3</span></div>
  <div class="row" style="top:2781px"><span class="code">E4</span><span class="name">Sausage</span><span class="price">5 ½ lb / 9 1lb</span></div>
  <div class="row" style="top:2839px"><span class="code">E5</span><span class="name">Sauce</span><span class="price">6 / cup</span></div>

  <div class="footer-mark">Gumbo's Crab Shack</div>
</body>
</html>
```